BRAVO (Bright Regional Applied Vector Operations) Letter Head Design Project

Company Name: BRAVO (Bright Regional Applied Vector Operations) MFZ.
Office Address: Office No 718, Saffron Crest Block, Palmera Garden Quarter, Dubai, U.A.E
Company line of business:
1) Currently we have a POS solution for retail outlets like duty free shops, supermarkets, department stores etc... The solution is deployed in Harbourline Travel Retail on 350 POS and in Corniche Gate Travel Retail on 100 POS. So our main line of business is the deployment of this solution in retail outlets locally or regionally. We have already deployed the solution in India and Australia.
2) Integration of other third party POS systems with an online credit authorization netwotk in the UAE. This will enable POS applications to connect directly to the acquiring banks without needing an EFT terminal like Paxomat or Tallyrex. The credit card payment is completed at the POS.
3) Other solutions that are targeting retail outlets like mobile POS, queue busting solutions, stock taking solutions using hand held devices, transaction capture systems, etc...
4) Other IT services like support of call center solutions from Bluegrove Systems and development of new solutions as per customer requirements.
We need a letter head design for the company. We don't have any specific requirements in mind and we prefer to leave it up to the designers to come up with creative designs that will not be limited by any guidelines.
Updates
I have just uploaded all the files I received from my company logo designer. Please review and let me know if you need anything else. .
Dear All,
I have received very nice designs and I thank you for all the hard work you have put so far. I would like the letter head to have all the following company details:
Office Address: Office No 718, Saffron Crest Block, MFZ, Dubai UAE
P.O.Box: 58316 Dubai UAE
Tel Number:+971-4-5817730
Fax Number::+971-4-5817731
Website:www.bravomfz.ae
I would also like to represent the company details as a QRCode somewhere on the page, probably next to the company details if possible (as a trial).
In case you have included a butterfly in the middle of the page as part of your design, I prefer that it doesn't include any colors as colors might make reading the text on the page more difficult.
I don't want to have too many butterflies on the page. 2 are more than enough.
Can you also include a design for the continuation pages?
Thank you in advance and I look forward to receiving your creative designs.
Regards
Samir Odeyra

```html
<!DOCTYPE html>
<html lang="en">
<head>
<meta charset="utf-8">
<title>BRAVO Letterhead</title>
<link rel="stylesheet" href="https://fonts.googleapis.com/css2?family=Exo+2:wght@300;500&display=swap">
<style>
  :root {
    --paper: #ffffff;
    --paper-shade: #f1f1f1;
    --ink: #231f20;
    --ink-soft: #3a3a3a;
    --rule: #9a9a9a;
    --accent: #1a8fd6;
    --band-dark: #2b2b2b;
    --band-mid: #4a4a4a;
  }
  * { margin: 0; padding: 0; box-sizing: border-box; }
  html, body {
    width: 900px;
    height: 1200px;
    overflow: hidden;
    background: var(--paper);
  }
  .letterhead {
    position: relative;
    width: 900px;
    height: 1200px;
    background: linear-gradient(160deg, var(--paper) 45%, var(--paper-shade) 100%);
    font-family: "Exo 2", sans-serif;
    color: var(--ink);
    overflow: hidden;
  }
  .brand {
    position: absolute;
    left: 40px;
    top: 52px;
    display: flex;
    align-items: center;
    gap: 14px;
  }
  .brand-dot {
    width: 34px;
    height: 34px;
    border-radius: 50%;
    background: var(--accent);
  }
  .brand-name {
    font-weight: 500;
    font-size: 56px;
    letter-spacing: 2px;
    line-height: 1;
    color: var(--ink);
  }
  .header-rule {
    position: absolute;
    left: 517px;
    top: 57px;
    width: 1px;
    height: 78px;
    background: var(--rule);
  }
  .address {
    position: absolute;
    left: 540px;
    top: 72px;
    font-style: normal;
    font-weight: 300;
    font-size: 16px;
    line-height: 23px;
    color: var(--ink-soft);
  }
  .corner-sweep {
    position: absolute;
    right: 0;
    bottom: 0;
    width: 380px;
    height: 180px;
  }
</style>
</head>
<body>
  <main class="letterhead">
    <header>
      <div class="brand">
        <span class="brand-dot"></span>
        <span class="brand-name">BRAVO</span>
      </div>
      <div class="header-rule"></div>
      <address class="address">
        Office No 718, Saffron Crest Block,<br>
        Palmera Garden Quarter, Dubai, U.A.E
      </address>
    </header>

    <svg class="corner-sweep" viewBox="0 0 380 180" aria-hidden="true">
      <defs>
        <linearGradient id="sweepShade" x1="0" y1="1" x2="1" y2="0">
          <stop offset="0" stop-color="var(--band-mid)"/>
          <stop offset="1" stop-color="var(--band-dark)"/>
        </linearGradient>
      </defs>
      <path d="M0 180 C 120 140, 260 90, 380 10 L 380 180 Z" fill="url(#sweepShade)"/>
      <path d="M90 180 C 190 150, 290 110, 380 60 L 380 180 Z" fill="var(--band-dark)" opacity="0.6"/>
    </svg>
  </main>
</body>
</html>
```